Business Card & Letterhead Design

We a financial advice company based in Australia. We provide advice to wealthy farmers.

We are changing our business name FROM Brightmere Financial TO Calderstone Wealth and we need a new letterhead and double sided business card design

Attached is designs from our previous branding (Brightmere Financial) as it includes all the details we require on the new Calderstone Wealth business cards and letterhead.

```html
<!DOCTYPE html>
<html lang="en">
<head>
<meta charset="utf-8">
<title>Calderstone Wealth Stationery</title>
<link href="https://fonts.googleapis.com/css2?family=Source+Sans+3:wght@400;600;700&family=Arimo:wght@400;700&display=swap" rel="stylesheet">
<style>
:root{
  --slate:#5a666b;
  --ink:#555f64;
  --faint:#eef0ef;
  --paper:#ffffff;
  --edge:#b9bdbf;
}
*{margin:0;padding:0;box-sizing:border-box}
html,body{width:1200px;height:1200px;overflow:hidden;background:var(--paper)}
body{position:relative;font-family:"Source Sans 3",sans-serif;color:var(--ink)}

.letterhead{position:absolute;left:285px;top:41px;width:671px;height:862px;border:1px solid var(--edge);background:var(--paper);overflow:hidden}
.brand{position:absolute;text-align:center}
.brand-ring{display:block;margin:0 auto;border-radius:50%;border:2px solid var(--slate)}
.brand-name{display:block;font-family:"Source Sans 3",sans-serif;font-weight:400;color:var(--slate);text-transform:uppercase;white-space:nowrap}
.letterhead .brand{left:52px;top:45px;width:172px}
.letterhead .brand-ring{width:47px;height:47px}
.letterhead .brand-name{font-size:15.5px;letter-spacing:.6px;margin-top:12px}

.side-bar{position:absolute;right:0;top:43px;width:8px;height:144px;background:var(--slate)}
.company-details{position:absolute;right:30px;top:44px;text-align:right;font-size:7px;line-height:9.6px;color:var(--ink)}
.company-details b{font-weight:700}
.company-details .gap{display:block;height:6px}
.company-details .sm-gap{display:block;height:3px}

.watermark{position:absolute;left:196px;top:544px;width:272px;height:272px}

.licensee{position:absolute;right:30px;top:773px;text-align:right;font-family:Arimo,sans-serif;color:var(--ink)}
.licensee .tag{font-size:9px;font-weight:700;letter-spacing:.3px;margin-bottom:9px}
.licensee p{font-size:6.6px;line-height:8px}
.licensee b{font-weight:700}

.foot-band{position:absolute;left:0;bottom:0;width:100%;height:12px;background:var(--slate)}
.foot-tab{position:absolute;left:243px;bottom:11px;width:185px;height:20px;background:var(--slate);border-radius:10px 10px 0 0;color:#fff;font-family:Arimo,sans-serif;font-weight:700;font-size:8px;letter-spacing:.9px;text-align:center;line-height:20px}

.card{position:absolute;top:967px;width:288px;height:172px}
.card-front{left:308px;background:var(--slate);color:#fff;text-align:center}
.card-front .brand{left:0;top:20px;width:100%}
.card-front .brand-ring{width:40px;height:40px;border-color:#fff}
.card-front .brand-name{font-size:9px;letter-spacing:1.4px;color:#fff;margin-top:7px;line-height:11px}
.services{position:absolute;left:0;top:92px;width:100%;font-size:8.3px;line-height:12.6px;letter-spacing:.8px}
.card-rule{position:absolute;left:22px;top:143px;width:240px;height:1px;background:rgba(255,255,255,.5)}
.card-front .legal{position:absolute;left:0;top:150px;width:100%;font-family:Arimo,sans-serif;font-size:6.6px;line-height:10px}

.card-back{left:602px;border:1px solid var(--edge);background:var(--paper)}
.card-back .brand{left:26px;top:23px;width:122px}
.card-back .brand-ring{width:33px;height:33px}
.card-back .brand-name{font-size:11px;letter-spacing:.3px;margin-top:6px}
.person{position:absolute;right:33px;top:73px;text-align:right}
.person .name{font-size:9.5px;font-weight:700;letter-spacing:1px;color:var(--slate)}
.person .creds{font-size:4px;letter-spacing:.2px}
.person .role{font-size:6.3px;line-height:9px;letter-spacing:.4px;margin-top:4px}
.card-back .card-rule{left:19px;top:120px;width:240px;background:var(--slate)}
.contacts{position:absolute;right:30px;top:125px;text-align:right;font-size:6px;line-height:10.5px;letter-spacing:.2px}
.contacts b{font-weight:700}
.contacts .sp{display:inline-block;width:10px}
.side-tab{position:absolute;right:-1px;top:31px;width:18px;height:123px;background:var(--slate);border-radius:8px 0 0 8px}
.side-tab span{position:absolute;left:50%;top:50%;transform:translate(-50%,-50%) rotate(-90deg);white-space:nowrap;color:#fff;font-family:Arimo,sans-serif;font-weight:700;font-size:5.6px;letter-spacing:.6px}
</style>
</head>
<body>

<section class="letterhead">
  <div class="brand">
    <span class="brand-ring"></span>
    <span class="brand-name">Calderstone Wealth</span>
  </div>

  <div class="side-bar"></div>
  <div class="company-details">
    Alderbank Holdings Pty Ltd<br>
    ATF The Redgum Family<br>
    Trust T/AS Brightmere Financial<br>
    ABN: 00 000 000 001<br>
    <b>Corporate Authorised</b><br>
    <b>Representative of Keystone</b><br>
    <b>Advisory Services Limited</b>
    <span class="gap"></span>
    Suite 4A, 18 Marlowe St<br>
    Riverton QLD 4000<br>
    PO Box 5120 - Riverton QLD 4000
    <span class="gap"></span>
    <b>p</b> (07) 3000 1234<br>
    <b>f</b> (07) 3000 5678
    <span class="sm-gap"></span>
    admin@<b>brightmerefinancial</b>.com.au<br>
    www.<b>brightmerefinancial</b>.com.au
  </div>

  <svg class="watermark" viewBox="0 0 272 272" aria-hidden="true">
    <circle cx="136" cy="136" r="131" fill="none" stroke="var(--faint)" stroke-width="9"/>
  </svg>

  <div class="licensee">
    <div class="tag">A referral built business</div>
    <p>Keystone Advisory Services Limited</p>
    <p>ABN 00 000 000 002</p>
    <p><b>Australian Financial Services Licence</b></p>
    <p><b>Licence Number 000 000</b></p>
    <p>Principle Address: 100 Harbour Rd</p>
    <p>PO Box 900 Melbourne VIC 3000</p>
  </div>

  <div class="foot-tab">'FINANCIAL PEACE OF MIND'</div>
  <div class="foot-band"></div>
</section>

<section class="card card-front">
  <div class="brand">
    <span class="brand-ring"></span>
    <span class="brand-name">Calderstone</span>
  </div>
  <div class="services">
    Personal &amp; Business Insurance Solutions<br>
    Business Estate Planning<br>
    Succession Planning
  </div>
  <div class="card-rule"></div>
  <div class="legal">
    Keystone Advisory Services Limited<br>
    Australian Financial Services Licensee License Number 000000
  </div>
</section>

<section class="card card-back">
  <div class="brand">
    <span class="brand-ring"></span>
    <span class="brand-name">Calderstone Wealth</span>
  </div>
  <div class="person">
    <div class="name">Tom Hale</div>
    <div class="creds">B.Ag.Ec. Dip F.P. CFP®</div>
    <div class="role">Managing Director<br>Authorised Representative</div>
  </div>
  <div class="card-rule"></div>
  <div class="contacts">
    <b>p</b> (07) 3000 1234<span class="sp"></span><b>f</b> (07) 3000 5678<span class="sp"></span><b>m</b> 0400 000 123<br>
    tom@<b>brightmerefinancial</b>.com.au<span class="sp"></span>www.<b>brightmerefinancial</b>.com.au<br>
    Suite 4A, 18 Marlowe St - Riverton QLD 4000<br>
    PO Box 5120 - Riverton QLD 4000
  </div>
  <div class="side-tab"><span>'FINANCIAL PEACE OF MIND'</span></div>
</section>

</body>
</html>
```